High-End audio shop owner needs a business card

I need a personal Business Card for my Audio shop which exists since 1962. We offer high Quality brands, professional Attention and run our own repair-service-department. I look for a design which will be printed on high Quality paper and shall convey trust to the Client that we are very serious. Language is german.

```html
<!DOCTYPE html>
<html lang="de">
<head>
<meta charset="utf-8">
<title>Hi-Fi Lindenhof – Visitenkarte</title>
<link href="https://fonts.googleapis.com/css2?family=Roboto:wght@400;700&family=Roboto+Condensed:wght@700&display=swap" rel="stylesheet">
<style>
  :root {
    --backdrop: #3a3a3c;
    --card: #232325;
    --card-edge: #1b1b1d;
    --photo-warm: #4a3a28;
    --photo-mid: #2b2520;
    --photo-dark: #121212;
    --orange: #ff6a00;
    --stripe-grey: #5f5f61;
    --text-grey: #c9c9c9;
  }
  * { box-sizing: border-box; margin: 0; padding: 0; }
  html, body { width: 799px; height: 1200px; overflow: hidden; }
  body {
    background: var(--backdrop);
    font-family: "Roboto", Arial, sans-serif;
    position: relative;
  }
  .card {
    position: absolute;
    left: 80px;
    width: 640px;
    height: 366px;
    background: var(--card);
    border: 1px solid var(--card-edge);
    box-shadow: 0 18px 40px rgba(0,0,0,.45);
    overflow: hidden;
  }
  .card--front { top: 150px; }
  .card--back { top: 690px; }

  .shop-photo {
    position: absolute;
    inset: 0;
    background:
      radial-gradient(ellipse at 70% 35%, rgba(120,85,45,.55) 0%, rgba(60,45,30,.25) 40%, transparent 70%),
      linear-gradient(160deg, var(--photo-warm) 0%, var(--photo-mid) 45%, var(--photo-dark) 100%);
  }
  .wordmark {
    font-family: "Roboto Condensed", "Arial Narrow", sans-serif;
    font-weight: 700;
    color: var(--orange);
    white-space: nowrap;
    letter-spacing: .5px;
  }
  .card--front .wordmark {
    position: absolute;
    left: 0; right: 0;
    top: 150px;
    text-align: center;
    font-size: 52px;
  }

  .accent-panel {
    position: absolute;
    left: 380px;
    top: 40px;
    right: 0;
    bottom: 0;
    background: linear-gradient(180deg, var(--stripe-grey) 0%, var(--orange) 45%, #b34c05 75%, var(--stripe-grey) 100%);
    opacity: .9;
  }

  .contact-block {
    position: absolute;
    left: 40px;
    top: 36px;
  }
  .person-name {
    font-family: "Roboto Condensed", "Arial Narrow", sans-serif;
    font-weight: 700;
    font-size: 21px;
    color: var(--orange);
  }
  .person-role {
    font-size: 14px;
    color: var(--text-grey);
    margin-top: 2px;
  }
  .contact-list {
    list-style: none;
    margin-top: 34px;
    font-size: 15px;
    color: var(--text-grey);
  }
  .contact-list li {
    display: flex;
    align-items: center;
    gap: 10px;
    height: 22px;
  }
  .contact-list svg { width: 13px; height: 13px; fill: var(--orange); flex: none; }
  .address {
    font-size: 15px;
    color: var(--text-grey);
    margin-top: 2px;
  }
  .card--back .wordmark {
    position: absolute;
    left: 40px;
    bottom: 46px;
    font-size: 36px;
  }
</style>
</head>
<body>
  <section class="card card--front">
    <div class="shop-photo" role="img" aria-label="Dunkles Foto des Hi-Fi-Geschäfts mit Lautsprechern und Regalen"></div>
    <div class="wordmark">Hi-Fi Lindenhof</div>
  </section>

  <section class="card card--back">
    <div class="accent-panel" role="img" aria-label="Grosses dekoratives Streifenelement in Orange und Grau"></div>
    <div class="contact-block">
      <div class="person-name">Anton Bachmann</div>
      <div class="person-role">Managing Director</div>
      <ul class="contact-list">
        <li>
          <svg viewBox="0 0 16 16" aria-hidden="true"><path d="M3 1h3l1.5 4-2 1.2a9 9 0 0 0 4.3 4.3L11 8.5l4 1.5v3c0 1-1 2-2 2A12 12 0 0 1 1 3c0-1 1-2 2-2z"/></svg>
          041 555 01 72
        </li>
        <li>
          <svg viewBox="0 0 16 16" aria-hidden="true"><path d="M1 3h14v10H1z M2 4l6 5 6-5" fill="none" stroke="#ff6a00" stroke-width="1.6"/></svg>
          hi@hifi-lh.ch
        </li>
        <li>
          <svg viewBox="0 0 16 16" aria-hidden="true"><circle cx="8" cy="8" r="6.5" fill="none" stroke="#ff6a00" stroke-width="1.5"/><path d="M1.5 8h13M8 1.5c-3 3.5-3 9.5 0 13M8 1.5c3 3.5 3 9.5 0 13" fill="none" stroke="#ff6a00" stroke-width="1.2"/></svg>
          www.hifi-lh.ch
        </li>
      </ul>
      <div class="address">Seeblickstrasse 12 CH-6003 Luzern</div>
    </div>
    <div class="wordmark">Hi-Fi Lindenhof</div>
  </section>
</body>
</html>
```